Business card for acupunctist in Melbourne. Specialises in Fertility, pre and post natal care, pain

I am looking for a business card which is going to catch people eyes. Two sided, one side in a muted colour (keeping it feminine) (pink or yellow???)maybe with a little simple logo or picture, the other side I was thinking white with 3 colours (pink grey and yellow... Had these in mind.
Info on the card
Maren Quillby Acupuncture

Dr Maren Quillby (TCM Acupuncture)
Acupuncture for balancing body and mind.
Verdant Osprey Clinic
14 Corran Lane, Eastwood 3071.
96274158
0438215074
Marentcm@quorvenmail.com

Some other little logo/ designs I have liked are as follows:
http://www.tessrolfeclinic.com/rates-and-insurance/
http://www.corabethwinslow.com/
http://www.zd-needlework.co.uk/

Target Market(s)

professional women, people in pain, active people, people seeking a healthy lifefstyle.

Industry/Entity Type

Business

Font styles to use
Serif
Sans Serif

Colors
eea4c8
fde08a
aaaaaa

Requirements
Must have
• Must be eye catching, but not too loud and busy. Subltle is good. Simple is also good. The logo could be something that represents growth and health and nurturing. Again not too elaborate, very simple.
Thankyou
Should not have
• Electric colours, crazy fonts, Pictures of yin and yang, candles, or bodies.

```html
<!DOCTYPE html>
<html lang="en">
<head>
<meta charset="utf-8">
<title>Maren Quillby Acupuncture – Business Card</title>
<link rel="stylesheet" href="https://fonts.googleapis.com/css2?family=Audiowide&family=Orbitron:wght@400&family=Yellowtail&family=Roboto:wght@400;500&display=swap">
<style>
  :root {
    --page-bg: #ececec;
    --yellow: #fde08a;
    --yellow-soft: #fbe7a8;
    --pink-light: #f6c6dd;
    --pink: #eea4c8;
    --pink-dusk: #d988b2;
    --pink-ink: #a9487f;
    --pink-ink-soft: #c06a9a;
    --grey: #aaaaaa;
    --grey-ink: #555555;
    --white: #ffffff;
    --card-shadow: rgba(0, 0, 0, 0.16);
  }
  * { box-sizing: border-box; margin: 0; padding: 0; }
  html, body {
    width: 1200px; height: 750px; overflow: hidden;
    background: var(--page-bg);
  }
  .canvas { position: relative; width: 1200px; height: 750px; }
  .card {
    position: absolute; top: 230px;
    width: 500px; height: 290px;
    border-radius: 26px; overflow: hidden;
    box-shadow: 0 6px 18px var(--card-shadow);
  }
  .card--front { left: 70px; }
  .card--back { left: 630px; }
  .card__bg { position: absolute; inset: 0; width: 100%; height: 100%; }

  .brand-name {
    position: absolute;
    font-family: "Audiowide", sans-serif;
    color: var(--pink-ink);
    white-space: nowrap;
  }
  .brand-rule { position: absolute; height: 2px; background: var(--grey); }
  .brand-trade {
    position: absolute;
    font-family: "Orbitron", sans-serif;
    font-weight: 400;
    color: var(--pink-ink-soft);
    white-space: nowrap;
    letter-spacing: 1px;
  }

  /* front */
  .card--front .brand-name { left: 52px; top: 98px; font-size: 34px; }
  .card--front .brand-rule { left: 52px; top: 148px; width: 360px; }
  .card--front .brand-trade { left: 48px; top: 162px; font-size: 54px; }

  /* back */
  .back-mark {
    position: absolute; left: 90px; top: 60px;
    width: 52px; height: 52px; border-radius: 50%;
    background: var(--pink);
  }
  .card--back .brand-name { left: 22px; top: 140px; font-size: 25px; }
  .card--back .brand-rule { left: 24px; top: 180px; width: 186px; }
  .card--back .brand-trade { left: 34px; top: 190px; font-size: 21px; }

  .practitioner {
    position: absolute; left: 262px; top: 26px;
    font-family: "Yellowtail", cursive;
    font-size: 28px; line-height: 1.1; color: var(--white); white-space: nowrap;
  }
  .practitioner__title {
    position: absolute; left: 290px; top: 62px;
    font-family: "Roboto", sans-serif; font-weight: 500;
    font-size: 11px; color: var(--pink-ink); letter-spacing: 0.5px;
  }
  .tagline {
    position: absolute; left: 258px; top: 84px; width: 226px;
    font-family: "Roboto", sans-serif;
    font-size: 10.5px; font-style: italic; color: var(--grey-ink);
  }
  .contact-list {
    position: absolute; left: 258px; top: 122px;
    list-style: none;
    font-family: "Roboto", sans-serif;
    font-size: 11.5px; color: var(--grey-ink); line-height: 1.5;
  }
  .contact-list li { display: flex; align-items: flex-start; gap: 6px; }
  .contact-list .clinic { font-weight: 500; color: var(--pink-ink); margin-bottom: 2px; }
  .contact-list svg { width: 11px; height: 11px; margin-top: 3px; flex: none; fill: var(--pink-ink); }
  .contact-list .indent { padding-left: 17px; }
</style>
</head>
<body>
<main class="canvas">

  <section class="card card--front" aria-label="Card front">
    <svg class="card__bg" viewBox="0 0 500 290" aria-hidden="true">
      <defs>
        <linearGradient id="frontPink" x1="0" y1="0" x2="1" y2="0">
          <stop offset="0" stop-color="#f6c6dd"/>
          <stop offset="1" stop-color="#d988b2"/>
        </linearGradient>
      </defs>
      <rect width="500" height="290" fill="url(#frontPink)"/>
      <path d="M0,64 C130,70 250,50 360,44 C395,42 405,84 445,86 L500,86 L500,290 L0,290 Z" fill="var(--yellow)"/>
    </svg>
    <div class="brand-name">Maren Quillby</div>
    <div class="brand-rule"></div>
    <div class="brand-trade">Acupuncture</div>
  </section>

  <section class="card card--back" aria-label="Card back">
    <svg class="card__bg" viewBox="0 0 500 290" aria-hidden="true">
      <defs>
        <linearGradient id="backPink" x1="0" y1="0" x2="1" y2="1">
          <stop offset="0" stop-color="#f6c6dd"/>
          <stop offset="0.6" stop-color="#eea4c8"/>
          <stop offset="1" stop-color="#d988b2"/>
        </linearGradient>
        <pattern id="dotRow" width="10" height="13" patternUnits="userSpaceOnUse">
          <circle cx="5" cy="6.5" r="2.4" fill="#eea4c8"/>
        </pattern>
      </defs>
      <rect width="500" height="290" fill="url(#backPink)"/>
      <rect width="232" height="290" fill="var(--yellow)"/>
      <rect x="227" y="0" width="10" height="290" fill="url(#dotRow)"/>
    </svg>

    <div class="back-mark"></div>
    <div class="brand-name">Maren Quillby</div>
    <div class="brand-rule"></div>
    <div class="brand-trade">Acupuncture</div>

    <div class="practitioner">Dr Maren Quillby</div>
    <div class="practitioner__title">TCM Acupuncture</div>
    <p class="tagline">Acupuncture for balancing body and mind.</p>

    <ul class="contact-list">
      <li class="clinic indent">Verdant Osprey Clinic</li>
      <li>
        <svg viewBox="0 0 12 12"><path d="M6 1 L11 6 H9.5 V11 H7 V8 H5 V11 H2.5 V6 H1 Z"/></svg>
        <span>14 Corran Lane, Eastwood 3071</span>
      </li>
      <li>
        <svg viewBox="0 0 12 12"><path d="M1 4 Q6 0 11 4 L10 6 L8 5 L8 4 Q6 3 4 4 L4 5 L2 6 Z M2.5 7 H9.5 V11 H2.5 Z"/></svg>
        <span>96274158</span>
      </li>
      <li>
        <svg viewBox="0 0 12 12"><path d="M3.5 0.5 H8.5 Q9 0.5 9 1 V11 Q9 11.5 8.5 11.5 H3.5 Q3 11.5 3 11 V1 Q3 0.5 3.5 0.5 Z M4 2 V9.5 H8 V2 Z"/></svg>
        <span>0438215074</span>
      </li>
      <li>
        <svg viewBox="0 0 12 12"><path d="M1 2.5 H11 V9.5 H1 Z M1.6 3 L6 6.5 L10.4 3 Z" fill-rule="evenodd"/></svg>
        <span>Marentcm@quorvenmail.com</span>
      </li>
    </ul>
  </section>

</main>
</body>
</html>
```